Business Card Design Project

Lumen Clinic Group

Dr Tomas Feldren M.D, F.R.C.S
Vascular and Vein Surgery

18-46 Corbell Avenue, Suite 317
Astoria
NY 11290

212-555-0163
718-555-0147
www.palemedic.example back of the card for scheduled appointments up to 5 appointment dates

Target Market(s)

Male and Female patients from 25 onwards with spider veins or varicose veins

Industry/Entity Type

Business

Font styles to use
Serif

Colors
86cae6
85abd2
0456a4

Requirements
Must have
• Modern Sophisticated design using light blue and grey text
Should not have
• hearts or flowers

```html
<!DOCTYPE html>
<html lang="en">
<head>
<meta charset="utf-8">
<title>Lumen Clinic Group – Business Card</title>
<link href="https://fonts.googleapis.com/css2?family=EB+Garamond:wght@400;600;700&display=swap" rel="stylesheet">
<style>
  :root {
    --front-light: #86cae6;
    --front-mid: #85abd2;
    --front-sky: #7fb0e4;
    --brand-blue: #0456a4;
    --band-light: #85abd2;
    --text-white: #ffffff;
    --text-soft: #eef3f9;
    --text-grey: #dfe7f1;
    --sheet: #ffffff;
  }
  * { margin: 0; padding: 0; box-sizing: border-box; }
  html, body { width: 1046px; height: 1200px; overflow: hidden; background: var(--sheet); }
  body { position: relative; font-family: "EB Garamond", Garamond, serif; }

  .card { position: absolute; left: 0; width: 1046px; overflow: hidden; }

  /* Front */
  .card-front {
    top: 0; height: 600px;
    background: linear-gradient(100deg, var(--front-sky) 0%, #9dc1e8 45%, #c9d7e6 75%, #d7dfe8 100%);
  }
  .front-decoration {
    position: absolute; right: 0; top: 0; width: 360px; height: 588px;
    background: linear-gradient(160deg, rgba(4,86,164,0.35) 0%, rgba(133,171,210,0.25) 60%, rgba(255,255,255,0.15) 100%);
  }
  .clinic-name {
    position: absolute; left: 96px; top: 118px;
    font-size: 64px; font-weight: 700; color: var(--brand-blue); line-height: 1; letter-spacing: -0.5px;
  }
  .clinic-mark {
    position: absolute; left: 100px; top: 200px; width: 22px; height: 22px; border-radius: 50%;
    background: var(--brand-blue);
  }
  .doctor-name {
    position: absolute; left: 96px; top: 298px;
    font-size: 35px; font-weight: 700; color: var(--text-white); line-height: 1;
  }
  .specialty {
    position: absolute; left: 96px; top: 340px;
    font-size: 27px; color: var(--text-soft); line-height: 1;
  }
  .divider {
    position: absolute; left: 96px; top: 384px; width: 525px; height: 2px; background: var(--text-white);
  }
  .contact-row {
    position: absolute; left: 96px; display: flex; align-items: center; gap: 20px;
    font-size: 28px; color: var(--text-soft); line-height: 1;
  }
  .contact-row.phone { top: 416px; }
  .contact-row.web { top: 461px; }
  .contact-icon { width: 30px; height: 30px; flex: none; }
  .address {
    position: absolute; left: 96px; top: 508px;
    font-size: 26px; line-height: 36px; color: var(--text-soft);
  }
  .front-band-dark { position: absolute; left: 0; top: 588px; width: 525px; height: 12px; background: var(--brand-blue); }
  .front-band-light { position: absolute; left: 525px; top: 588px; width: 521px; height: 12px; background: var(--band-light); }

  /* Back */
  .card-back { top: 606px; height: 594px; background: var(--brand-blue); }
  .back-decoration {
    position: absolute; left: 370px; top: 50px; width: 310px; height: 500px; border-radius: 50% 50% 8px 8px;
    background: radial-gradient(ellipse at 50% 40%, rgba(133,171,210,0.22), rgba(133,171,210,0) 70%);
  }
  .appointment-title {
    position: absolute; left: 0; width: 100%; top: 90px; text-align: center;
    font-size: 37px; font-weight: 700; color: var(--text-grey); text-decoration: underline;
    text-decoration-thickness: 2px; text-underline-offset: 5px; letter-spacing: 0.5px; line-height: 1;
  }
  .slot { position: absolute; font-size: 22px; line-height: 33.5px; color: var(--text-grey); }
  .slot-line { display: flex; white-space: nowrap; }
  .slot-label { width: 70px; }
  .slot-dots { letter-spacing: 1.2px; }
  .slot.top-left { left: 60px; top: 177px; }
  .slot.top-right { left: 679px; top: 177px; }
  .slot.mid-left { left: 60px; top: 316px; }
  .slot.mid-right { left: 679px; top: 316px; }
  .slot.bottom-center { left: 370px; top: 463px; }
  .back-band { position: absolute; left: 0; bottom: 0; width: 100%; height: 8px; background: var(--band-light); }
</style>
</head>
<body>

<section class="card card-front">
  <div class="front-decoration" role="img" aria-label="Soft blue gradient area where the large brand symbol decoration sits"></div>
  <span class="clinic-mark"></span>
  <div class="clinic-name">Lumen Clinic Group</div>

  <div class="doctor-name">Dr Tomas Feldren M.D, F.R.C.S</div>
  <div class="specialty">Vascular and Vein Surgery</div>
  <div class="divider"></div>

  <div class="contact-row phone">
    <svg class="contact-icon" viewBox="0 0 30 30" aria-hidden="true">
      <rect x="0" y="0" width="30" height="30" rx="4" fill="#0456a4"/>
      <rect x="10" y="5" width="10" height="20" rx="1.5" fill="none" stroke="#fff" stroke-width="1.6"/>
      <rect x="12" y="8" width="6" height="5" fill="#fff"/>
      <circle cx="13" cy="16" r="0.9" fill="#fff"/><circle cx="15" cy="16" r="0.9" fill="#fff"/><circle cx="17" cy="16" r="0.9" fill="#fff"/>
      <circle cx="13" cy="19" r="0.9" fill="#fff"/><circle cx="15" cy="19" r="0.9" fill="#fff"/><circle cx="17" cy="19" r="0.9" fill="#fff"/>
    </svg>
    <span>212-555-0163 | 718-555-0147</span>
  </div>
  <div class="contact-row web">
    <svg class="contact-icon" viewBox="0 0 30 30" aria-hidden="true">
      <rect x="0" y="0" width="30" height="30" rx="4" fill="#0456a4"/>
      <g fill="none" stroke="#fff" stroke-width="1.5">
        <circle cx="15" cy="15" r="10"/>
        <ellipse cx="15" cy="15" rx="4.5" ry="10"/>
        <line x1="5" y1="15" x2="25" y2="15"/>
        <path d="M7 10 H23 M7 20 H23"/>
      </g>
    </svg>
    <span>www.palemedic.example</span>
  </div>

  <div class="address">
    18-46 Corbell Avenue, Suite 317<br>
    Astoria, NY 11290
  </div>

  <div class="front-band-dark"></div>
  <div class="front-band-light"></div>
</section>

<section class="card card-back">
  <div class="back-decoration" role="img" aria-label="Faint lighter blue glow where the brand symbol watermark sits"></div>
  <div class="appointment-title">APPOINTMENT</div>

  <div class="slot top-left">
    <div class="slot-line"><span class="slot-label">Date:</span><span class="slot-dots">............................</span></div>
    <div class="slot-line"><span class="slot-label">Time:</span><span class="slot-dots">...........................</span></div>
    <div class="slot-line"><span class="slot-label">Name:</span><span class="slot-dots">...........................</span></div>
  </div>
  <div class="slot top-right">
    <div class="slot-line"><span class="slot-label">Date:</span><span class="slot-dots">............................</span></div>
    <div class="slot-line"><span class="slot-label">Time:</span><span class="slot-dots">...........................</span></div>
    <div class="slot-line"><span class="slot-label">Name:</span><span class="slot-dots">...........................</span></div>
  </div>
  <div class="slot mid-left">
    <div class="slot-line"><span class="slot-label">Date:</span><span class="slot-dots">............................</span></div>
    <div class="slot-line"><span class="slot-label">Time:</span><span class="slot-dots">...........................</span></div>
    <div class="slot-line"><span class="slot-label">Name:</span><span class="slot-dots">...........................</span></div>
  </div>
  <div class="slot mid-right">
    <div class="slot-line"><span class="slot-label">Date:</span><span class="slot-dots">............................</span></div>
    <div class="slot-line"><span class="slot-label">Time:</span><span class="slot-dots">...........................</span></div>
    <div class="slot-line"><span class="slot-label">Name:</span><span class="slot-dots">...........................</span></div>
  </div>
  <div class="slot bottom-center">
    <div class="slot-line"><span class="slot-label">Date:</span><span class="slot-dots">............................</span></div>
    <div class="slot-line"><span class="slot-label">Time:</span><span class="slot-dots">...........................</span></div>
    <div class="slot-line"><span class="slot-label">Name:</span><span class="slot-dots">...........................</span></div>
  </div>

  <div class="back-band"></div>
</section>

</body>
</html>
```